Business card for a business coach / management consultant

My logo has been done and now I need a business card. Deliverable needs to be a PDF to give to the printer. I want it single sided as I want the back side blank.
I prefer a white card with modern simple professional design.
Details are:
Dale Whitford
B.Sc. (hons) FRLT CP MNBQR
7 Corrigan Rd
Kestrel Vale WA 6099
Australia
mobile 040 31 582 47
email dale@ventureharbor.example.au
skype dalewhitfordnorth
Small to medium size business owners
Business

```html
<!DOCTYPE html>
<html lang="en">
<head>
<meta charset="utf-8">
<title>Dale Whitford – Business Card</title>
<link rel="stylesheet" href="https://fonts.googleapis.com/css2?family=Titillium+Web:wght@400;600&display=swap">
<style>
  :root {
    --card-white: #ffffff;
    --brand-red: #c1272d;
    --ink: #5b1a14;
    --arc-1: #efd3cb;
    --arc-2: #e5b2a5;
    --arc-3: #da8c7b;
    --arc-4: #cc5c4e;
    --logo-line: #ffffff;
  }
  html, body {
    margin: 0;
    padding: 0;
    width: 1200px;
    height: 900px;
    overflow: hidden;
    background: var(--card-white);
  }
  .card {
    position: relative;
    width: 1200px;
    height: 900px;
    font-family: "Titillium Web", sans-serif;
    color: var(--ink);
  }
  .card-art {
    position: absolute;
    inset: 0;
  }
  .identity {
    position: absolute;
    left: 134px;
    top: 176px;
  }
  .identity-name {
    margin: 0;
    font-size: 46px;
    font-weight: 600;
    line-height: 1;
    color: var(--brand-red);
    letter-spacing: 0.5px;
  }
  .identity-credentials {
    margin: 8px 0 0;
    font-size: 26px;
    font-weight: 400;
    line-height: 1.1;
  }
  .address {
    position: absolute;
    left: 134px;
    top: 490px;
    margin: 0;
    font-style: normal;
    font-size: 23px;
    line-height: 36px;
  }
  .contact-list {
    position: absolute;
    left: 142px;
    top: 630px;
    margin: 0;
    padding: 0;
    list-style: none;
    font-size: 23px;
    line-height: 36px;
  }
  .contact-item {
    display: flex;
    align-items: center;
    gap: 18px;
  }
  .contact-icon {
    width: 30px;
    height: 24px;
    flex: none;
  }
  .logo-label {
    position: absolute;
    left: 798px;
    top: 448px;
    width: 280px;
    transform: translateY(-50%);
    text-align: center;
    font-size: 30px;
    font-weight: 400;
    letter-spacing: 2.5px;
    color: var(--logo-line);
  }
</style>
</head>
<body>
<div class="card">
  <svg class="card-art" width="1200" height="900" viewBox="0 0 1200 900" aria-hidden="true">
    <defs>
      <clipPath id="card-edge">
        <rect x="0" y="132" width="1124" height="634"/>
      </clipPath>
    </defs>
    <g clip-path="url(#card-edge)">
      <circle cx="1276" cy="450" r="618" fill="var(--arc-1)"/>
      <circle cx="1300" cy="450" r="618" fill="var(--arc-2)"/>
      <circle cx="1324" cy="450" r="618" fill="var(--arc-3)"/>
      <circle cx="1346" cy="450" r="618" fill="var(--arc-4)"/>
      <circle cx="1370" cy="450" r="618" fill="var(--brand-red)"/>
    </g>
    <circle class="logo-ring" cx="938" cy="448" r="140" fill="none" stroke="var(--logo-line)" stroke-width="3"/>
  </svg>

  <header class="identity">
    <h1 class="identity-name">Dale Whitford</h1>
    <p class="identity-credentials">B.Sc. (hons) FRLT CP MNBQR</p>
  </header>

  <address class="address">
    7 Corrigan Rd<br>
    Kestrel Vale WA 6099<br>
    Australia
  </address>

  <ul class="contact-list">
    <li class="contact-item">
      <svg class="contact-icon" viewBox="0 0 30 24" aria-label="Mobile" role="img">
        <path d="M3 8c0-3 5-5 12-5s12 2 12 5v2h-6V7.5c-2-.7-4-1-6-1s-4 .3-6 1V10H3z" fill="var(--ink)"/>
        <path d="M8 11l3-3h8l3 3v9H8z" fill="var(--ink)"/>
        <circle cx="15" cy="15" r="2.5" fill="var(--card-white)"/>
      </svg>
      <span>040 31 582 47</span>
    </li>
    <li class="contact-item">
      <svg class="contact-icon" viewBox="0 0 30 24" aria-label="Email" role="img">
        <rect x="2" y="3" width="26" height="18" fill="none" stroke="var(--ink)" stroke-width="2.2"/>
        <path d="M2 3l13 11L28 3M2 21l10-9M28 21l-10-9" fill="none" stroke="var(--ink)" stroke-width="2.2"/>
      </svg>
      <span>dale@ventureharbor.example.au</span>
    </li>
    <li class="contact-item">
      <svg class="contact-icon" viewBox="0 0 30 24" aria-label="Chat handle" role="img">
        <circle cx="15" cy="12" r="8" fill="var(--ink)"/>
      </svg>
      <span>dalewhitfordnorth</span>
    </li>
  </ul>

  <div class="logo-label">LOGO HERE</div>
</div>
</body>
</html>
```